2 page brouchure for a Property Valuation company.

We require a 2 page brochure (printed front and back) for a property valuation company known as 'Brookmere Valuations'.

Brookmere valuations provides independent, reliable, accurate valuation services to our clients on the value of their properties to enable confidence and certainty in their decision.

The brochure is to be used to convey that the company provides valuation services for 8 main purposes and across 4 different property types.

The 8 main purposes for valuation include:
- Pre-Purchase Valuations
- Stamp Duty Valuations
-Capital Gains Tax (CGT)Valuations
-Unit Entitlement Valuations
-Family Law and Litigation Valuations
-Easement Valuations
-Wills & Probate Valuations
-Insolvency/Asset Realisation Valuations

The 4 main property types are:
-Residential
-Commercial
-Industrial
-Retail.

The brochure should have a title page, a page for the services, a page for the property types and a rear page with contact details.
Contact detail will include;
email:
phone :
Post :
website:

The words 'property valuation and advisory services' should be used at the front of the brochure.

The brochure should be professional and is used to convey information using visual aid and is to be used for promotion.

Our main colors are dark green and grey as seen in our logo.

We have attached our logo to add to the brochure and visit our website at: www.brookmerevaluations-example.com.au for more information about the company.

Please let me know if there are any further questions.

Target Market(s)

Solicitors/Lawyers
Accountants
Surveyors
Builders/Developers

Requirements
Must have
• Logo Colors, Logo, 8 Main services, 4 main property types, contact details.
Nice to have
• Should have concise visual aids to convey message.

Please add that we provide fast 48 hour turnaround for short form valuations. Maybe use a visual aid to convey this.

```html
<!DOCTYPE html>
<html lang="en">
<head>
<meta charset="utf-8">
<title>Brookmere Valuations – Brochure</title>
<link href="https://fonts.googleapis.com/css2?family=Oswald:wght@300;400;500;600&family=Montserrat:wght@500;600;700&display=swap" rel="stylesheet">
<style>
  :root{
    --green:#0d6a35;
    --green-dark:#0a5a2c;
    --grey-dark:#3a3b3d;
    --grey-text:#3b3c3e;
    --white:#ffffff;
    --bg:#f2f2f2;
  }
  *{box-sizing:border-box;margin:0;padding:0}
  html,body{width:901px;height:1200px;overflow:hidden;background:var(--bg)}
  .canvas{position:relative;width:901px;height:1200px}
  .page{position:absolute;top:302px;width:420px;height:595px;background:var(--white);overflow:hidden;box-shadow:0 2px 6px rgba(0,0,0,.25)}
  .page--types{left:18px}
  .page--services{left:463px}
  .abs{position:absolute}
  .condensed{font-family:"Oswald",sans-serif;text-transform:uppercase}

  /* Property types page */
  .hero-photo{left:0;top:0;width:420px;height:320px;border-bottom-right-radius:70px;
    background:linear-gradient(160deg,#f4f6f4 0%,#dfe5df 40%,#c9d2c4 65%,#eef0ee 100%)}
  .types-banner{left:0;top:320px;width:295px;height:46px;background:var(--green);border-top-right-radius:14px;
    color:var(--white);font-size:22px;font-weight:500;line-height:46px;padding-left:18px;letter-spacing:.3px}
  .city-photo{left:0;top:366px;width:420px;height:162px;
    background:linear-gradient(90deg,#f7f4ef 0%,#efeae2 45%,#b9c4cc 70%,#5c7791 100%)}
  .type-list{left:40px;top:372px;list-style:none}
  .type-list li{font-size:22px;font-weight:500;color:var(--grey-text);line-height:35px;position:relative;padding-left:16px}
  .type-list li::before{content:"";position:absolute;left:0;top:15px;width:7px;height:7px;border-radius:50%;background:var(--grey-text)}
  .contact-band{left:0;top:528px;width:245px;height:67px;background:var(--green);color:var(--white);
    font-family:"Montserrat",sans-serif;text-align:center;padding-top:16px}
  .contact-band .small{font-size:6.4px;font-weight:600;line-height:11px}
  .contact-band .web{font-size:8.4px;font-weight:700;line-height:13px}
  .phone-block{left:245px;top:528px;width:175px;height:67px;text-align:center;font-family:"Montserrat",sans-serif;color:var(--grey-text);padding-top:18px}
  .phone-block .label{font-size:7px;font-weight:600}
  .phone-block .number{font-size:16px;font-weight:600}

  /* Services page */
  .side-column{left:28px;top:0;width:142px;height:100px;background:var(--grey-dark)}
  .brand{left:170px;top:0;width:250px;height:100px;display:flex;align-items:center;justify-content:center;gap:10px}
  .brand-mark{width:18px;height:18px;background:var(--green)}
  .brand-name{font-family:"Montserrat",sans-serif;font-weight:600;font-size:15px;color:var(--grey-text);letter-spacing:2.5px;text-transform:uppercase}
  .grass-photo{left:0;top:100px;width:170px;height:219px;border-top-left-radius:40px;background:linear-gradient(180deg,#b9cfae 0%,#6f9b52 60%,#4f7f34 100%)}
  .title-panel{left:28px;top:100px;width:142px;height:219px;background:rgba(13,106,53,.92);color:var(--white);text-align:center;padding-top:38px}
  .title-panel .light{font-weight:300;font-size:25px;line-height:29px;display:block}
  .title-panel .bold{font-weight:600;font-size:29px;line-height:31px;display:block}
  .family-photo{left:170px;top:100px;width:250px;height:219px;border-bottom-right-radius:50px;
    background:linear-gradient(180deg,#c8d3d8 0%,#a9b8c0 40%,#8fb06d 75%,#79a84d 100%)}
  .law-photo{left:28px;top:319px;width:142px;height:97px;background:linear-gradient(135deg,#f2ece4 0%,#c9a98a 60%,#8a6a52 100%)}
  .savings-photo{left:28px;top:416px;width:142px;height:106px;border-bottom-left-radius:32px;background:linear-gradient(180deg,#9cc37a 0%,#5f9440 60%,#b08a66 100%)}
  .purposes{left:183px;top:324px}
  .purposes h2{font-family:"Oswald",sans-serif;font-weight:500;font-size:14px;color:var(--green);text-transform:uppercase;margin-bottom:4px;letter-spacing:.2px}
  .purpose-list{list-style:none}
  .purpose-list li{display:flex;align-items:center;gap:7px;font-family:"Oswald",sans-serif;font-size:11px;color:var(--grey-text);text-transform:uppercase;height:21.5px}
  .purpose-list svg{width:12px;height:12px;flex:none}
  .turnaround{left:170px;top:527px;width:250px;height:68px;background:var(--grey-dark);color:var(--white);text-align:center;font-family:"Montserrat",sans-serif;padding-top:4px}
  .turnaround .lead{font-size:15px;font-weight:600;line-height:17px}
  .turnaround .big{font-size:34px;font-weight:500;line-height:32px;letter-spacing:.5px}
  .turnaround .note{font-size:6.3px;font-weight:600;line-height:9px}
</style>
</head>
<body>
<div class="canvas">

  <section class="page page--types">
    <div class="abs hero-photo" role="img" aria-label="Model house with rolled plans and a laptop on a bright desk"></div>
    <h2 class="abs types-banner condensed">The 4 Main Property Types</h2>
    <div class="abs city-photo" role="img" aria-label="Tall glass office towers seen from below"></div>
    <ul class="abs type-list condensed">
      <li>Residential</li>
      <li>Commercial</li>
      <li>Industrial</li>
      <li>Retail</li>
    </ul>
    <div class="abs contact-band">
      <p class="small">EMAIL: INFO@BROOKMEREVALUATIONS-EXAMPLE.COM.AU</p>
      <p class="small">MAIL: PO BOX 418 ASHFIELD VALE NSW 2199</p>
      <p class="web">WWW.BROOKMEREVALUATIONS-EXAMPLE.COM.AU</p>
    </div>
    <div class="abs phone-block">
      <p class="label">PHONE:</p>
      <p class="number">1300 555 014</p>
    </div>
  </section>

  <section class="page page--services">
    <div class="abs side-column"></div>
    <div class="abs brand">
      <span class="brand-mark"></span>
      <span class="brand-name">Brookmere Valuations</span>
    </div>
    <div class="abs grass-photo" role="img" aria-label="Green lawn in a sunny garden"></div>
    <div class="abs family-photo" role="img" aria-label="Family lying on the lawn in front of their house"></div>
    <h1 class="abs title-panel condensed">
      <span class="light">Property</span>
      <span class="bold">Valuation</span>
      <span class="light">and</span>
      <span class="bold">Advisory</span>
      <span class="light">Services</span>
    </h1>
    <div class="abs law-photo" role="img" aria-label="Statue of justice with scales on an office desk"></div>
    <div class="abs savings-photo" role="img" aria-label="Hand stacking coins in rising piles"></div>
    <div class="abs purposes">
      <h2>The 8 Main Purposes for Valuation</h2>
      <ul class="purpose-list">
        <li><svg viewBox="0 0 12 12"><circle cx="6" cy="6" r="6" fill="#0d6a35"/><path d="M3 6.3 6 3.6 9 6.3M4.2 5.5V8.5H7.8V5.5" fill="none" stroke="#fff" stroke-width="1"/></svg>Pre-Purchase Valuations</li>
        <li><svg viewBox="0 0 12 12"><circle cx="6" cy="6" r="6" fill="#0d6a35"/><text x="6" y="8.6" font-size="7.5" font-family="Montserrat,sans-serif" font-weight="700" fill="#fff" text-anchor="middle">$</text></svg>Stamp Duty Valuations</li>
        <li><svg viewBox="0 0 12 12"><circle cx="6" cy="6" r="6" fill="#0d6a35"/><path d="M3.5 8.5V7M5.2 8.5V5.8M6.9 8.5V4.6M8.6 8.5V3.5" stroke="#fff" stroke-width="1.1"/></svg>Capital Gains Tax (CGT)Valuations</li>
        <li><svg viewBox="0 0 12 12"><circle cx="6" cy="6" r="6" fill="#0d6a35"/><rect x="4" y="3" width="4" height="6" fill="none" stroke="#fff" stroke-width="1"/><path d="M5 4.5h2M5 6h2M5 7.5h2" stroke="#fff" stroke-width=".6"/></svg>Unit Entitlement Valuations</li>
        <li><svg viewBox="0 0 12 12"><circle cx="6" cy="6" r="6" fill="#0d6a35"/><path d="M3.5 8.5 6.5 5.5M5.8 3.8 8.2 6.2" stroke="#fff" stroke-width="1.3"/></svg>Family Law and Litigation Valuations</li>
        <li><svg viewBox="0 0 12 12"><circle cx="6" cy="6" r="6" fill="#0d6a35"/><rect x="3" y="3.8" width="6" height="4.4" fill="none" stroke="#fff" stroke-width="1"/><path d="M4.3 5.3h3.4M4.3 6.7h3.4" stroke="#fff" stroke-width=".6"/></svg>Easement Valuations</li>
        <li><svg viewBox="0 0 12 12"><circle cx="6" cy="6" r="6" fill="#0d6a35"/><path d="M4 3h3l1.2 1.2V9H4z" fill="none" stroke="#fff" stroke-width="1"/></svg>Wills &amp; Probate Valuations</li>
        <li><svg viewBox="0 0 12 12"><circle cx="6" cy="6" r="6" fill="#0d6a35"/><path d="M3.2 5 4.5 3.5h3L8.8 5 6 8.8z" fill="none" stroke="#fff" stroke-width="1"/></svg>Insolvency/Asset Realisation Valuations</li>
      </ul>
    </div>
    <div class="abs turnaround">
      <p class="lead">WE PROVIDE FAST</p>
      <p class="big">48 HOUR</p>
      <p class="note">TURNAROUND FOR SHORT FORM VALUATIONS</p>
    </div>
  </section>

</div>
</body>
</html>
```